Website Design Requirements

Domain Name: HometownTradesfolkRegistry.com

Website Look: Simple, Clean, Modern, and Professional Awarding Winning Website. Our Platform is the Best Directory Platform, all we need is a very creative person to make the following designs and select the fonts, font sizing, font colors and all the colors for the color points. We will follow up with the winner of the contest to design the rest of our design needs. The highlight of our brand is our Mascot; we feel this is something everyone will remember. It may be the easiest to obtain a free trial of the platform from Vantory Listings to complete this project. When we pick a winner of this contest we will provide the password to our admin panel for everything to be applied. Our Competitors are Perrows Hub, Yardwise Pro and Gravelnook.

We are thinking a light gray scale shadowing or graduated ghosting for the background behind the image of the Mascot for the main image. We want the Mascot and the Selection box to stand out as well as the logo.

Design Elements:
Main Page Image-Size for website is 1800 X 600px should be the Mascot on the right half of the image; this is where creative design is the most important. Design can use the head only from the waist up or the full image

Logo- Size for website is 450 X 70px; the logo should have the head of the mascot on a 3D icon with 2 line of text to the right side. The top line should have Hometown Tradesfolk the second line should have the word Directory in smaller size and be ghosted. The main idea about the logo is the icon and the words Hometown Tradesfolk. Note example can be seen on the Vantory Listings Rapid Launch Walkthrough on Clip Vue.

Favicon- Size for website is 56 X 56px should be the head of the mascot the Favicon and Google Map Pin drop could be the same if design is nice enough

Google Map Pin Drop- 25 X 46px should be the head of the mascot with a arrow pointing down.

Member Badge Image- Size 250 X 250px should be the head of the mascot inside a round ring with the words Verified –Certified –Member.

Target Market(s)

Consumers will use this website to locate Contractors in their Local area. Contractors will list their business on this website for a fee.

Industry/Entity Type

Domain

Contact Information for Business Card

Marcus Oldfield
Partner
555.014.2871
Marcus@HometownTradesfolkRegistry.Com
WWW. HometownTradesfolkRegistry.com

Logo Text

Hometown Tradesfolk Registry

Number of Pages Required

3 page

Font styles to use
Serif

Colors
ec1f27
fbed22

Requirements
Must have
• The use of our mascot, you can use full body view, waist up or head shot
Nice to have
• Clean bright colored Mascot, listing on back of card
• Hometown Tradesfolk
• Electricians
• Plumbers
• HVAC
• Landscapers
• General Contractors
• Garage Door Repair
• Carpet Cleaners
• Concrete Contractors

```html
<!DOCTYPE html>
<html lang="en">
<head>
<meta charset="utf-8">
<title>Find Top Rated Hometown Tradesfolk Near You</title>
<link href="https://fonts.googleapis.com/css2?family=Raleway:wght@300;400;700&family=Alfa+Slab+One&display=swap" rel="stylesheet">
<style>
  :root {
    --sky-light: #a9a9a9;
    --sky-mid: #7b7b7b;
    --ground-dark: #2e2e2e;
    --heading-dark: #2a2a2a;
    --heading-outline: #e9e9e9;
    --panel-bg: rgba(58, 58, 58, 0.82);
    --panel-border: #5e5e5e;
    --field-bg: #ffffff;
    --field-text: #3a3a3a;
    --icon-color: #4a1410;
    --button-bg: #f8b800;
    --button-text: #ffffff;
    --mascot-red: #d9302a;
    --mascot-blue: #3f6fa8;
    --mascot-skin: #f2b27c;
  }
  * { box-sizing: border-box; margin: 0; padding: 0; }
  html, body { width: 1200px; height: 400px; overflow: hidden; background: var(--ground-dark); }
  .hero {
    position: relative;
    width: 1200px;
    height: 400px;
    overflow: hidden;
    font-family: "Raleway", sans-serif;
  }
  .hero-backdrop {
    position: absolute;
    inset: 0;
    background:
      radial-gradient(ellipse 520px 300px at 330px 170px, rgba(230,230,230,0.55), rgba(230,230,230,0) 70%),
      linear-gradient(180deg, var(--sky-mid) 0%, var(--sky-light) 35%, #6c6c6c 60%, var(--ground-dark) 100%);
  }
  .mascot {
    position: absolute;
    left: 232px;
    top: 16px;
    width: 170px;
    height: 376px;
    border-radius: 70px 70px 24px 24px;
    background: linear-gradient(180deg, #f4c430 0%, var(--mascot-skin) 18%, var(--mascot-red) 32%, var(--mascot-red) 58%, var(--mascot-blue) 70%, var(--mascot-blue) 90%, #9a6a2a 100%);
    opacity: 0.9;
  }
  .headline {
    position: absolute;
    left: 483px;
    top: 40px;
    color: var(--heading-dark);
  }
  .headline-lead,
  .headline-tail {
    display: block;
    font-weight: 300;
    font-size: 24px;
    line-height: 1;
    letter-spacing: 0.5px;
    text-transform: uppercase;
    text-shadow: 0 0 1px var(--heading-outline);
  }
  .headline-main {
    display: block;
    font-family: "Alfa Slab One", serif;
    font-size: 36px;
    line-height: 1.05;
    margin: 4px 0 6px;
    text-transform: uppercase;
    text-shadow: 2px 2px 0 var(--heading-outline);
  }
  .search-panel {
    position: absolute;
    left: 485px;
    top: 154px;
    width: 385px;
    height: 195px;
    background: var(--panel-bg);
    border: 2px solid var(--panel-border);
    border-radius: 4px;
    padding: 15px 0 0 23px;
  }
  .search-field {
    display: flex;
    align-items: center;
    width: 339px;
    height: 35px;
    background: var(--field-bg);
    border-radius: 3px;
    padding-left: 18px;
    margin-bottom: 16px;
    font-size: 12px;
    color: var(--field-text);
  }
  .search-field svg { width: 11px; height: 11px; margin-right: 9px; fill: var(--icon-color); }
  .search-button {
    display: flex;
    align-items: center;
    justify-content: center;
    width: 339px;
    height: 42px;
    margin-top: 6px;
    background: var(--button-bg);
    border-radius: 3px;
    color: var(--button-text);
    font-weight: 700;
    font-size: 12.5px;
    letter-spacing: 0.3px;
    text-transform: uppercase;
  }
</style>
</head>
<body>
<section class="hero">
  <div class="hero-backdrop" role="img" aria-label="Grey sunburst rays over a city skyline silhouette with construction cranes"></div>
  <div class="mascot" role="img" aria-label="Cartoon contractor mascot in a yellow hard hat, red shirt and jeans with a tool belt, arms crossed"></div>

  <h1 class="headline">
    <span class="headline-lead">Find Top Rated</span>
    <span class="headline-main">Hometown Tradesfolk</span>
    <span class="headline-tail">Near You!</span>
  </h1>

  <form class="search-panel">
    <div class="search-field">
      <svg viewBox="0 0 16 16" aria-hidden="true"><path d="M6.5 1a5.5 5.5 0 0 1 4.4 8.8l4 4-1.4 1.4-4-4A5.5 5.5 0 1 1 6.5 1zm0 2a3.5 3.5 0 1 0 0 7 3.5 3.5 0 0 0 0-7z"/></svg>
      <span>Enter Keyword</span>
    </div>
    <div class="search-field">
      <svg viewBox="0 0 16 16" aria-hidden="true"><path d="M8 0a5 5 0 0 1 5 5c0 4-5 11-5 11S3 9 3 5a5 5 0 0 1 5-5zm0 3a2 2 0 1 0 0 4 2 2 0 0 0 0-4z"/></svg>
      <span>Enter City or Post Code</span>
    </div>
    <div class="search-button">Search Now</div>
  </form>
</section>
</body>
</html>
```